Velnora - Quality health delivered at your door

Velnora offers home and Community Based Services for adults who wish to continue live independently in their communities. We increase accessibility to health care, reduce health care delivery gap, reduce mortality and morbidity, reduce health while promoting healthy living in the comfort of our patients communities or homes.

We provide on site services and deliver high quality healthcare at your door. Our experienced physicians coordinate care with our certified nurse practitioners and provide chronic care management, physical therapy, rehabilitation and medications management.

Target Market(s)

Older population living in independent living facilities

Industry/Entity Type

Health Care

Contact Information for Business Card

Velnora

Number of Pages Required

4 page

Font styles to use
Sans Serif

Colors

Designer to choose colors to be used in the design.

```html
<!DOCTYPE html>
<html lang="en">
<head>
<meta charset="utf-8">
<title>Velnora - Quality health delivered at your door</title>
<link href="https://fonts.googleapis.com/css2?family=PT+Sans:wght@400;700&family=Marcellus&family=Lora:ital@1&display=swap" rel="stylesheet">
<style>
:root{
  --green-dark:#263807;
  --green-label:#3a4c0d;
  --orange:#f7941d;
  --orange-deep:#f39a13;
  --ink:#2b2b2b;
  --muted:#7a7a7a;
  --white:#ffffff;
}
*{box-sizing:border-box;margin:0;padding:0}
html,body{width:1200px;height:2821px;overflow:hidden;background:var(--white)}
body{position:relative;font-family:"PT Sans",sans-serif;color:var(--ink)}
.abs{position:absolute}

/* top bar */
.topbar{left:0;top:0;width:1200px;height:117px;background:var(--green-dark);border-top:4px solid var(--orange)}
.follow{left:77px;top:28px;color:var(--white);font-size:16px}
.social{display:flex;gap:9px}
.social span{width:34px;height:34px;border-radius:50%;background:var(--orange);display:block}
.social.outline span{background:transparent;border:2px solid var(--orange)}
.top-social{left:79px;top:54px}
.brand-badge{left:514px;top:-32px;width:172px;height:172px;border-radius:50%;background:var(--white);z-index:3}
.brand-name{left:514px;top:82px;width:172px;text-align:center;font-family:"Marcellus",serif;font-size:21px;color:var(--green-dark);z-index:4}
.call{left:912px;top:30px;display:flex;gap:14px;align-items:center}
.call small{display:block;color:var(--white);font-size:15px}
.call strong{display:block;color:var(--orange);font-size:26px;letter-spacing:1px}

/* nav */
.nav{left:0;top:117px;width:1200px;height:62px;background:var(--white);box-shadow:0 3px 4px rgba(0,0,0,.25);display:flex;align-items:center;padding-left:77px;z-index:2}
.nav a{font-size:14px;color:#444;text-decoration:none;text-transform:uppercase;padding:0 13px;height:62px;line-height:62px}
.nav a.active{background:var(--orange);color:var(--white)}

/* hero */
.hero-photo{left:0;top:179px;width:780px;height:519px;background:linear-gradient(90deg,#b99f86 0%,#d8c3ae 35%,#6c8fb0 55%,#eef1f2 85%,#fff 100%)}
.hero-eyebrow{left:675px;top:284px;font-family:"Lora",serif;font-style:italic;font-size:25px;color:var(--orange)}
.hero-title{left:677px;top:328px;font-size:45px;line-height:57px;font-weight:700;color:var(--ink)}
.btn{display:flex;align-items:center;justify-content:center;background:var(--orange);color:var(--white);font-size:22px;text-transform:uppercase}
.hero-btn{left:679px;top:506px;width:192px;height:56px}
.dots{left:1153px;top:371px;display:flex;flex-direction:column;gap:11px}
.dots span{width:18px;height:18px;border-radius:50%;border:2px solid var(--orange)}
.dots span.on{background:var(--orange)}

/* welcome */
.welcome{left:0;top:698px;width:1200px;height:369px;background:var(--green-dark);text-align:center;color:#e6e9dc}
.section-title{font-family:"Marcellus",serif;font-size:38px;color:var(--orange);text-transform:uppercase}
.welcome .section-title{margin-top:55px}
.welcome p{font-size:14px;line-height:24px;width:820px;margin:10px auto 0}
.welcome-btn{left:512px;top:248px;width:176px;height:57px}

/* services */
.services-title{left:0;top:1125px;width:1200px;text-align:center}
.services-lead{left:290px;top:1186px;width:620px;text-align:center;font-size:14px;line-height:27px;color:var(--muted)}
.grid{left:77px;top:1258px;display:grid;grid-template-columns:repeat(4,250px);column-gap:15.5px;row-gap:35px}
.grid.row3{top:1806px}
.card{width:250px;height:249px}
.card .photo{height:189px}
.card .label{height:60px;background:var(--green-label);color:var(--white);font-size:15px;line-height:22px;text-align:center;display:flex;align-items:center;justify-content:center;text-transform:uppercase}
.card .label.plain{text-transform:none}
.card.featured .label{background:var(--orange)}

/* consultation */
.consult-photo{left:600px;top:2120px;width:600px;height:519px;background:linear-gradient(120deg,#e9e4dc 0%,#d7c9b8 40%,#9fb8b0 60%,#c9b29a 100%)}
.consult-panel{left:0;top:2120px;width:600px;height:519px;background:var(--orange-deep)}
.consult-arrow{left:596px;top:2300px}
.consult-frame{left:11px;top:2133px;width:578px;height:497px;border:1px solid rgba(255,255,255,.6)}
.consult-title{left:77px;top:2178px;font-family:"Marcellus",serif;font-size:36px;color:var(--white)}
.field{left:77px;width:459px;height:45px;border:1px solid rgba(255,255,255,.7);color:var(--white);font-size:14px;padding:0 14px;line-height:43px}
.submit{left:77px;top:2530px;width:156px;height:56px;border:2px solid var(--white);color:var(--white);font-family:"Marcellus",serif;font-size:20px;display:flex;align-items:center;justify-content:center}

/* footer */
.footer{left:0;top:2639px;width:1200px;height:182px;background:var(--green-dark);color:var(--white)}
.foot-label{left:77px;top:46px;color:var(--orange);font-size:14px}
.foot-line{left:77px;display:flex;align-items:center;gap:18px;font-size:15px}
.foot-badge{left:556px;top:47px;width:88px;height:88px;border-radius:50%;background:#4c6a12;border:4px solid var(--white)}
.foot-name{left:450px;top:135px;width:300px;text-align:center;font-family:"Marcellus",serif;font-size:30px;color:var(--green-label);color:#5f7d1a}
.foot-social{left:934px;top:62px}
.copyright{left:800px;top:113px;width:313px;text-align:right;font-size:14px}
</style>
</head>
<body>

<header class="abs topbar">
  <div class="abs follow">Follow Us :</div>
  <div class="abs social top-social"><span></span><span></span><span></span><span></span></div>
  <div class="abs call">
    <svg width="44" height="46" viewBox="0 0 24 24"><path fill="#f7941d" d="M6.6 10.8a15.1 15.1 0 0 0 6.6 6.6l2.2-2.2c.3-.3.7-.4 1-.2 1.1.4 2.3.6 3.6.6.6 0 1 .4 1 1V20c0 .6-.4 1-1 1A17 17 0 0 1 3 4c0-.6.4-1 1-1h3.5c.6 0 1 .4 1 1 0 1.3.2 2.5.6 3.6.1.3 0 .7-.2 1z"/></svg>
    <div><small>Call Us Today :</small><strong>123 456 7890</strong></div>
  </div>
</header>
<div class="abs brand-badge"></div>
<div class="abs brand-name">VELNORA</div>

<nav class="abs nav">
  <a class="active">Home</a><a>Assisted Living</a><a>Skilled Nursing</a><a>Independent Living</a><a>Services</a><a>Respite Care</a><a>Rehabilitation</a><a>Oriel Learning Center</a>
</nav>

<section>
  <div class="abs hero-photo" role="img" aria-label="Smiling senior woman embracing a caregiver in blue scrubs"></div>
  <div class="abs hero-eyebrow">We Provide You</div>
  <h1 class="abs hero-title">Services &amp; Deliver High<br>Quality Healthcare At<br>Your Door.</h1>
  <div class="abs btn hero-btn">Contact Us</div>
  <div class="abs dots"><span></span><span></span><span></span><span class="on"></span><span></span></div>
</section>

<section class="abs welcome">
  <h2 class="section-title">Welcome to Velnora</h2>
  <p>Velnora offers home and Community Based Services for adults who wish to continue to live independently in the comfort of their communities.</p>
  <p>We provide on site services and deliver high quality healthcare at your door.&nbsp; Our experienced physicians coordinate care with our certified nurse practitioners and provide chronic care management, physical therapy, rehabilitation and medications management.</p>
  <div class="abs btn welcome-btn">Know More</div>
</section>

<h2 class="abs section-title services-title">Our Best Services</h2>
<p class="abs services-lead">Lorem Ipsum is simply dummy text of the printing and typesetting industry. Lorem Ipsum has been the industry's standard dummy text ever since the rinter took a galley of type and scrambled it t.</p>

<div class="abs grid">
  <div class="card featured"><div class="photo" role="img" aria-label="Doctor reviewing a tablet with a patient" style="background:linear-gradient(135deg,#d9c6a8,#8a6a4a)"></div><div class="label">Comprehensive<br>Primary Care</div></div>
  <div class="card"><div class="photo" role="img" aria-label="Caregiver helping a senior with a walker" style="background:linear-gradient(135deg,#eee9e2,#b9b0a6)"></div><div class="label">Coordination of<br>Speciality Care</div></div>
  <div class="card"><div class="photo" role="img" aria-label="Nurse checking a patient's blood pressure" style="background:linear-gradient(135deg,#e6e2dc,#9a8572)"></div><div class="label">Chronic Disease<br>Management</div></div>
  <div class="card"><div class="photo" role="img" aria-label="Nurse reviewing notes with a senior man" style="background:linear-gradient(135deg,#cdbfae,#8c7c6e)"></div><div class="label">Transitional<br>Care</div></div>
  <div class="card"><div class="photo" role="img" aria-label="Nurse visiting a woman at home" style="background:linear-gradient(135deg,#d7d9d6,#5f7a96)"></div><div class="label">Skilled Nursing<br>Visits</div></div>
  <div class="card"><div class="photo" role="img" aria-label="Holding the hands of an elderly person" style="background:linear-gradient(135deg,#5a4536,#b8937a)"></div><div class="label">Social Services<br>Assessment</div></div>
  <div class="card"><div class="photo" role="img" aria-label="Aide helping a senior walk in a hallway" style="background:linear-gradient(135deg,#b8a58a,#6a5640)"></div><div class="label">Home Health<br>Assistance</div></div>
  <div class="card"><div class="photo" role="img" aria-label="Therapist stretching a patient's leg" style="background:linear-gradient(135deg,#e4e2de,#8f8f8f)"></div><div class="label">Physical<br>Therapy</div></div>
</div>
<div class="abs grid row3">
  <div class="card"><div class="photo" role="img" aria-label="Nurse talking with a senior woman" style="background:linear-gradient(135deg,#6a4a3a,#2c7f86)"></div><div class="label">Mental Health</div></div>
  <div class="card"><div class="photo" role="img" aria-label="Dental team with a smiling patient" style="background:linear-gradient(135deg,#f1eeea,#9fb8c8)"></div><div class="label">Dental Health</div></div>
  <div class="card"><div class="photo" role="img" aria-label="Senior boarding a transport van" style="background:linear-gradient(135deg,#e9e9e9,#6d6f74)"></div><div class="label">Transportation</div></div>
  <div class="card"><div class="photo" role="img" aria-label="Caregivers comforting an elderly woman" style="background:linear-gradient(135deg,#e8e1d6,#9c7f6e)"></div><div class="label plain">Alzheimer's disease<br>management</div></div>
</div>

<section>
  <div class="abs consult-photo" role="img" aria-label="Nurse caring for a senior woman in a wheelchair"></div>
  <div class="abs consult-panel"></div>
  <svg class="abs consult-arrow" width="30" height="102" viewBox="0 0 30 102"><polygon points="0,0 28,51 0,102" fill="#f39a13"/></svg>
  <div class="abs consult-frame"></div>
  <h2 class="abs consult-title">FREE CONSULTATION</h2>
  <div class="abs field" style="top:2250px">Name*</div>
  <div class="abs field" style="top:2305px">Email*</div>
  <div class="abs field" style="top:2359px">Phone*</div>
  <div class="abs field" style="top:2415px">Services*
    <svg class="abs" style="right:14px;top:17px" width="18" height="10" viewBox="0 0 18 10"><polygon points="0,0 18,0 9,10" fill="#fff"/></svg></div>
  <div class="abs field" style="top:2472px">Address*</div>
  <div class="abs submit">SUBMIT</div>
</section>

<footer class="abs footer">
  <div class="abs foot-label">Call Or Email Us :</div>
  <div class="abs foot-line" style="top:78px">
    <svg width="22" height="22" viewBox="0 0 24 24"><path fill="#f7941d" d="M6.6 10.8a15.1 15.1 0 0 0 6.6 6.6l2.2-2.2c.3-.3.7-.4 1-.2 1.1.4 2.3.6 3.6.6.6 0 1 .4 1 1V20c0 .6-.4 1-1 1A17 17 0 0 1 3 4c0-.6.4-1 1-1h3.5c.6 0 1 .4 1 1 0 1.3.2 2.5.6 3.6.1.3 0 .7-.2 1z"/></svg>
    <span>123 456 7890</span></div>
  <div class="abs foot-line" style="top:112px">
    <svg width="22" height="16" viewBox="0 0 22 16"><rect width="22" height="16" fill="#f7941d"/><polyline points="1,1 11,9 21,1" fill="none" stroke="#263807" stroke-width="2"/></svg>
    <span>info@velnora.com</span></div>
  <div class="abs foot-badge"></div>
  <div class="abs foot-name">VELNORA</div>
  <div class="abs social outline foot-social"><span style="background:var(--orange);border:none"></span><span></span><span></span><span></span></div>
  <div class="abs copyright">©<b>VELNORA</b> -2017 All rights reserved.</div>
</footer>

</body>
</html>
```